Rebranding our business - Business Cards

We are currently rebranding our business and have just completed our new logo and now are wanting to have new business cards designed.

I will upload our old business card design as we would like to keep the same information on the card, Including the icon dot points on the back. I will also upload other designs I would like placed on the cards.. Such as a character,

I would like our power statement to be:
KTW Removals -The Gentle Movers.

Instead of: Allow KTW Removals To Carry the Weight Of Every Relocation,

I am happy for the designer to run with their own ideas.

```html
<!DOCTYPE html>
<html lang="en">
<head>
<meta charset="utf-8">
<title>KTW Removals – Business Cards</title>
<link href="https://fonts.googleapis.com/css2?family=Open+Sans:wght@400;600;700&display=swap" rel="stylesheet">
<style>
  :root{
    --navy:#16256b;
    --orange:#f0712c;
    --white:#ffffff;
    --paper:#fbfbfb;
    --backdrop:#e9e6e1;
    --ink:#1b1b1b;
  }
  *{box-sizing:border-box;margin:0;padding:0}
  html,body{width:1200px;height:900px;overflow:hidden}
  body{background:var(--backdrop);font-family:"Open Sans",Arial,sans-serif;position:relative}
  .card{position:absolute;left:285px;width:630px;height:360px;background:var(--paper);overflow:hidden;box-shadow:0 6px 18px rgba(0,0,0,.18)}
  .card--back{top:60px}
  .card--front{top:480px}

  /* back */
  .services{position:absolute;top:0;left:0;right:0;height:205px;text-align:center;padding-top:34px;color:var(--ink)}
  .services__title{font-size:16px;font-weight:700;color:var(--navy);letter-spacing:.3px;margin-bottom:14px}
  .services__title span{color:var(--orange)}
  .services__line{font-size:18px;font-weight:700;line-height:30px}
  .dot{display:inline-block;width:11px;height:11px;border-radius:50%;background:var(--navy);margin:0 7px;vertical-align:1px}
  .rule{position:absolute;left:0;right:0;height:8px;background:var(--orange)}
  .panel{position:absolute;left:0;right:0;bottom:0;background:var(--navy);color:var(--white)}
  .card--back .rule{top:205px}
  .card--back .panel{top:216px}
  .insurance{position:absolute;top:20px;left:0;right:0;text-align:center;font-size:16px;font-weight:700;letter-spacing:.3px}
  .contact{position:absolute;display:flex;flex-direction:column;gap:8px;font-size:16px}
  .contact__row{display:flex;align-items:center;gap:12px;white-space:nowrap;line-height:22px}
  .contact__row svg{flex:none}
  .card--back .contact--phones{top:62px;left:140px}
  .card--back .contact--web{top:62px;left:335px}

  /* front */
  .brand{position:absolute;top:0;left:0;right:0;height:160px;display:flex;align-items:center;justify-content:center;gap:12px}
  .brand__mark{width:16px;height:16px;border-radius:50%;background:var(--orange)}
  .brand__name{font-size:38px;font-weight:700;color:var(--navy);letter-spacing:.2px}
  .card--front .rule{top:160px}
  .card--front .panel{top:168px}
  .tagline{position:absolute;top:18px;left:0;width:340px;height:32px;background:var(--orange);display:flex;align-items:center;justify-content:center;font-size:14px;font-weight:700;letter-spacing:.3px;text-transform:uppercase;white-space:nowrap}
  .address{position:absolute;top:24px;left:360px;font-size:14px;white-space:nowrap}
  .person{position:absolute;top:60px;left:70px}
  .person__name{font-size:24px;font-weight:700;line-height:28px}
  .person__role{font-size:16px;line-height:20px;padding-left:30px}
  .card--front .contact--phones{top:118px;left:110px;gap:6px;font-size:17px}
  .card--front .contact--web{top:60px;left:350px;gap:8px;font-size:15px}
  .social-dot{width:10px;height:10px;border-radius:50%;background:var(--white);margin:0 3px}
</style>
</head>
<body>

<section class="card card--back" aria-label="Business card, reverse side">
  <div class="services">
    <p class="services__title">KTW REMOVALS <span>PROVIDES:</span></p>
    <p class="services__line">Local,Country &amp; Interstate Removals</p>
    <p class="services__line">Home &amp; Hi Rise Removals<span class="dot"></span>Office &amp; Factory Relocation's</p>
    <p class="services__line">Pre - Packing &amp; Unpacking Service's<span class="dot"></span>Storage Solution</p>
  </div>
  <div class="rule"></div>
  <div class="panel">
    <p class="insurance">FREE TRANSIT INSURANCE!</p>
    <div class="contact contact--phones">
      <p class="contact__row">
        <svg width="14" height="14" viewBox="0 0 24 24" aria-hidden="true"><path fill="#fff" d="M6.6 10.8a15.1 15.1 0 0 0 6.6 6.6l2.2-2.2c.3-.3.7-.4 1-.2 1.1.4 2.3.6 3.6.6.6 0 1 .4 1 1V20c0 .6-.4 1-1 1A17 17 0 0 1 3 4c0-.6.4-1 1-1h3.5c.6 0 1 .4 1 1 0 1.3.2 2.5.6 3.6.1.3 0 .7-.2 1z"/></svg>
        0400 312 786
      </p>
      <p class="contact__row">
        <svg width="14" height="14" viewBox="0 0 24 24" aria-hidden="true"><rect x="6" y="2" width="12" height="20" rx="2" fill="none" stroke="#fff" stroke-width="2.4"/><line x1="10" y1="18" x2="14" y2="18" stroke="#fff" stroke-width="2"/></svg>
        07 5500 4812
      </p>
    </div>
    <div class="contact contact--web">
      <p class="contact__row">
        <svg width="16" height="12" viewBox="0 0 24 18" aria-hidden="true"><rect x="1" y="1" width="22" height="16" rx="1.5" fill="#fff"/><path d="M2 2l10 8 10-8" fill="none" stroke="#16256b" stroke-width="2"/></svg>
        ktwremovals@mailbox.com
      </p>
      <p class="contact__row">
        <svg width="16" height="16" viewBox="0 0 24 24" aria-hidden="true"><path d="M10 14a4 4 0 0 0 5.7 0l3.5-3.5a4 4 0 0 0-5.7-5.7L12 6.3M14 10a4 4 0 0 0-5.7 0l-3.5 3.5a4 4 0 0 0 5.7 5.7l1.5-1.5" fill="none" stroke="#fff" stroke-width="2.4" stroke-linecap="round"/></svg>
        www.ktwremovals.com.au
      </p>
    </div>
  </div>
</section>

<section class="card card--front" aria-label="Business card, front side">
  <div class="brand">
    <span class="brand__mark"></span>
    <span class="brand__name">KTW Removals</span>
  </div>
  <div class="rule"></div>
  <div class="panel">
    <p class="tagline">KTW Removals -The Gentle Movers.</p>
    <p class="address">Harbour Point,QLD 4000</p>
    <div class="person">
      <p class="person__name">Rowan Hale</p>
      <p class="person__role">Owner Operator</p>
    </div>
    <div class="contact contact--phones">
      <p class="contact__row">
        0400 312 786
        <svg width="16" height="16" viewBox="0 0 24 24" aria-hidden="true"><path fill="#fff" d="M6.6 10.8a15.1 15.1 0 0 0 6.6 6.6l2.2-2.2c.3-.3.7-.4 1-.2 1.1.4 2.3.6 3.6.6.6 0 1 .4 1 1V20c0 .6-.4 1-1 1A17 17 0 0 1 3 4c0-.6.4-1 1-1h3.5c.6 0 1 .4 1 1 0 1.3.2 2.5.6 3.6.1.3 0 .7-.2 1z"/></svg>
      </p>
      <p class="contact__row">
        07 5500 4812
        <svg width="16" height="16" viewBox="0 0 24 24" aria-hidden="true"><rect x="6" y="2" width="12" height="20" rx="2" fill="none" stroke="#fff" stroke-width="2.4"/><line x1="10" y1="18" x2="14" y2="18" stroke="#fff" stroke-width="2"/></svg>
      </p>
    </div>
    <div class="contact contact--web">
      <p class="contact__row">
        <svg width="16" height="12" viewBox="0 0 24 18" aria-hidden="true"><rect x="1" y="1" width="22" height="16" rx="1.5" fill="#fff"/><path d="M2 2l10 8 10-8" fill="none" stroke="#16256b" stroke-width="2"/></svg>
        ktwremovals@mailbox.com
      </p>
      <p class="contact__row">
        <svg width="16" height="16" viewBox="0 0 24 24" aria-hidden="true"><path d="M10 14a4 4 0 0 0 5.7 0l3.5-3.5a4 4 0 0 0-5.7-5.7L12 6.3M14 10a4 4 0 0 0-5.7 0l-3.5 3.5a4 4 0 0 0 5.7 5.7l1.5-1.5" fill="none" stroke="#fff" stroke-width="2.4" stroke-linecap="round"/></svg>
        www.ktwremovals.com.au
      </p>
      <p class="contact__row">
        <span class="social-dot"></span>
        www.social.example/ktwremovals
      </p>
    </div>
  </div>
</section>

</body>
</html>
```